Employees at R&T Gale Power Services need new modern business cards

We need new business cards that showcase our new rebranded logo. We are seeking modern, clean, fresh, attractive cards while still being professional. We want to stand out. A little bit about us: we work in Canada and the USA. We offer Technical Field Advisors to support wind turbine manufacturers through the construction phase of wind farms. I am attaching a mock inspiration picture to lead you in the direction we want to see this go. Also, FYI We have approx. 10/11 different employees that would need their own card. Let me know when you would need everyone's name. We would love to see some black and white options as well as color copies- when using colors we want green to be the dominant color with accents for blue and orange (colors should match our logo). I have also attached copies of our old business card for reference.

Contact Information for Business Card

Name, Telephone, Email, address, company name, website. EXAMPLE: Dean Whitlock, DeanWhitlock@randtgale.net, 555-384-9162, 318276 Fallow Line #7, Marrowby, ON X9Z 4Q2, www.randtgale.net

Colors
0054AA
0677BA
7BADD7
CADEEF
E8F1F8
00AB8E
00BBA5
67D7C9
C6EFE9
E9F9F6
F0912C
F2A743
F7CA91
FBE8D2
FDF5EE

Requirements
Must have
• 2 sided business card

```html
<!DOCTYPE html>
<html lang="en">
<head>
<meta charset="utf-8">
<title>R&amp;T Gale Power Services – Business Card</title>
<link rel="stylesheet" href="https://fonts.googleapis.com/css2?family=Open+Sans:wght@400;600&display=swap">
<style>
  :root {
    --backdrop: #ababab;
    --card-white: #ffffff;
    --ink-dark: #1a1a1a;
    --ink-muted: #6b6b6b;
    --divider: #c9c9c9;
    --accent-orange: #f2a31b;
    --accent-green: #1ea82f;
    --accent-blue: #0677ba;
    --brand-green: #22a83a;
    --grad-yellow: #f8b41c;
    --grad-green: #1ba52e;
    --grad-blue: #0e7fc0;
  }
  * { box-sizing: border-box; margin: 0; padding: 0; }
  html, body { width: 1200px; height: 1000px; overflow: hidden; }
  body {
    position: relative;
    background: var(--backdrop);
    font-family: "Open Sans", Arial, sans-serif;
  }
  .card {
    position: absolute;
    left: 294px;
    width: 613px;
    height: 352px;
    border-radius: 24px;
    overflow: hidden;
    box-shadow: 0 18px 40px rgba(0,0,0,0.28);
  }
  .card--front { top: 118px; background: var(--card-white); }
  .card--back { top: 532px; }

  /* Front */
  .brand-lockup {
    position: absolute;
    left: 52px; top: 100px;
    width: 230px;
    display: flex;
    flex-direction: column;
    align-items: center;
    gap: 14px;
  }
  .brand-lockup__dot {
    width: 76px; height: 76px;
    border-radius: 50%;
    background: var(--brand-green);
  }
  .brand-lockup__name {
    font-size: 17px;
    font-weight: 600;
    color: var(--brand-green);
    text-align: center;
    letter-spacing: 0.5px;
    line-height: 1.2;
  }
  .card__divider {
    position: absolute;
    left: 306px; top: 108px;
    width: 2px; height: 156px;
    background: var(--divider);
  }
  .contact-block {
    position: absolute;
    left: 335px; top: 110px;
  }
  .contact-block__name {
    font-size: 23px;
    font-weight: 400;
    color: var(--ink-dark);
    line-height: 30px;
  }
  .contact-block__role {
    font-size: 21px;
    color: var(--accent-orange);
    line-height: 30px;
    margin-bottom: 12px;
  }
  .contact-list { list-style: none; }
  .contact-list__item {
    display: flex;
    align-items: center;
    gap: 8px;
    font-size: 16px;
    color: var(--ink-muted);
    height: 26px;
  }
  .contact-list__icon { width: 13px; height: 13px; flex: none; }

  /* Back */
  .back-field {
    position: absolute; inset: 0;
    background:
      radial-gradient(ellipse 340px 200px at 50% 105%, var(--grad-blue) 0%, rgba(14,127,192,0.6) 45%, rgba(14,127,192,0) 100%),
      linear-gradient(100deg, var(--grad-yellow) 0%, #e9b21c 22%, #8db62c 45%, var(--grad-green) 68%, var(--grad-green) 100%);
  }
  .back-lockup {
    position: absolute;
    left: 277px; top: 216px;
    display: flex;
    align-items: center;
    gap: 12px;
  }
  .back-lockup__dot {
    width: 56px; height: 56px;
    border-radius: 50%;
    background: var(--card-white);
  }
  .back-lockup__name {
    font-size: 17px;
    font-weight: 600;
    color: var(--card-white);
    letter-spacing: 0.5px;
    line-height: 1.15;
  }
</style>
</head>
<body>
  <section class="card card--front" aria-label="Business card front">
    <div class="brand-lockup">
      <div class="brand-lockup__dot"></div>
      <div class="brand-lockup__name">R&amp;T GALE<br>POWER SERVICES</div>
    </div>
    <div class="card__divider"></div>
    <div class="contact-block">
      <p class="contact-block__name">Dean Whitlock</p>
      <p class="contact-block__role">Owner</p>
      <ul class="contact-list">
        <li class="contact-list__item">
          <svg class="contact-list__icon" viewBox="0 0 16 16" aria-hidden="true"><path fill="#0677ba" d="M3.5 1.5l2.5 0 1 3.5-1.7 1.2c.8 1.8 2.3 3.3 4.1 4.1L10.6 8.6l3.5 1V12c0 1.2-1 2-2.2 2C6.5 13.6 2.4 9.5 2 4.1 2 2.6 2.5 1.5 3.5 1.5z"/></svg>
          <span>555-384-9162</span>
        </li>
        <li class="contact-list__item">
          <svg class="contact-list__icon" viewBox="0 0 16 16" aria-hidden="true"><rect x="1" y="3" width="14" height="10" rx="1" fill="#f2a31b"/><path d="M1.5 3.8L8 9l6.5-5.2" fill="none" stroke="#fff" stroke-width="1.3"/></svg>
          <span>deanwhitlock@randtgale.net</span>
        </li>
        <li class="contact-list__item">
          <svg class="contact-list__icon" viewBox="0 0 16 16" aria-hidden="true"><circle cx="8" cy="8" r="7" fill="#1ea82f"/><path d="M1 8h14M8 1c-2.6 3-2.6 11 0 14M8 1c2.6 3 2.6 11 0 14M2.5 4.5h11M2.5 11.5h11" fill="none" stroke="#fff" stroke-width="0.9"/></svg>
          <span>www.randtgale.net</span>
        </li>
      </ul>
    </div>
  </section>

  <section class="card card--back" aria-label="Business card back">
    <div class="back-field" role="img" aria-label="Gradient background from yellow to green and blue, where a faint repeating pattern belongs"></div>
    <div class="back-lockup">
      <div class="back-lockup__dot"></div>
      <div class="back-lockup__name">R&amp;T GALE<br>POWER SERVICES</div>
    </div>
  </section>
</body>
</html>
```